Checkout sign

Wall sign for clinic checkout.
“The Good Lord does ALL the healing..
But we DO collect the co-pay”

Add Celtic cross at top and our logo on bottom

```html
<!DOCTYPE html>
<html lang="en">
<head>
<meta charset="utf-8">
<title>Checkout Sign – Brennan Orthopedic Clinic</title>
<link rel="stylesheet" href="https://fonts.googleapis.com/css2?family=Bebas+Neue&family=Oswald:wght@200&display=swap">
<style>
  :root {
    --ink-blue: #1e0091;
    --paper: #ffffff;
  }
  html, body {
    margin: 0;
    padding: 0;
    width: 1200px;
    height: 1000px;
    overflow: hidden;
    background: var(--paper);
  }
  .checkout-sign {
    display: block;
    width: 1200px;
    height: 1000px;
  }
  .sweep { fill: var(--ink-blue); }
  .rule { fill: var(--ink-blue); }
  .headline {
    font-family: "Bebas Neue", "Oswald", sans-serif;
    font-size: 90px;
  }
  .subline {
    font-family: "Oswald", sans-serif;
    font-weight: 200;
    font-size: 82px;
  }
  .on-white { fill: var(--ink-blue); }
  .on-blue { fill: var(--paper); }
  .cross-ring { fill: none; stroke: var(--ink-blue); stroke-width: 12; }
  .cross-beam { fill: var(--ink-blue); }
  .clinic-mark { fill: none; stroke: var(--ink-blue); stroke-width: 6; }
  .clinic-name {
    font-family: "Bebas Neue", sans-serif;
    fill: var(--ink-blue);
    text-anchor: middle;
  }
</style>
</head>
<body>
<svg class="checkout-sign" viewBox="0 0 1200 1000" xmlns="http://www.w3.org/2000/svg" role="img" aria-label="Checkout sign: The good Lord does all the healing, but we do collect the co-pay">
  <defs>
    <path id="sweep-shape" d="M85,0 L682,0 C560,140 490,300 508,470 C528,680 700,880 910,1000 L155,1000 C70,860 -25,660 -12,470 C-5,300 30,150 85,0 Z"/>
    <clipPath id="sweep-clip"><use href="#sweep-shape"/></clipPath>
  </defs>

  <rect width="1200" height="1000" fill="var(--paper)"/>
  <use href="#sweep-shape" class="sweep"/>

  <!-- celtic cross -->
  <g class="celtic-cross">
    <polygon class="cross-beam" points="1036,30 1054,30 1054,160 1060,210 1030,210 1036,160"/>
    <rect class="cross-beam" x="984" y="74" width="125" height="22"/>
    <circle class="cross-ring" cx="1045" cy="85" r="42"/>
  </g>

  <!-- rules -->
  <rect class="rule" x="527" y="373" width="228" height="7"/>
  <rect class="rule" x="669" y="649" width="396" height="7"/>

  <!-- quote, blue on white -->
  <g class="quote on-white">
    <text class="headline" x="34" y="492" textLength="1150" lengthAdjust="spacingAndGlyphs">“THE GOOD LORD DOES ALL THE HEALING..</text>
    <text class="subline" x="181" y="605" textLength="1005" lengthAdjust="spacingAndGlyphs">BUT WE DO COLLECT THE CO-PAY”</text>
  </g>
  <!-- quote, white over the blue sweep -->
  <g class="quote on-blue" clip-path="url(#sweep-clip)">
    <text class="headline" x="34" y="492" textLength="1150" lengthAdjust="spacingAndGlyphs">“THE GOOD LORD DOES ALL THE HEALING..</text>
    <text class="subline" x="181" y="605" textLength="1005" lengthAdjust="spacingAndGlyphs">BUT WE DO COLLECT THE CO-PAY”</text>
  </g>

  <!-- clinic name -->
  <g class="clinic">
    <circle class="clinic-mark" cx="1045" cy="833" r="66"/>
    <text class="clinic-name" x="1045" y="938" font-size="44" letter-spacing="2">BRENNAN</text>
    <text class="clinic-name" x="1045" y="966" font-size="24" letter-spacing="1.5">ORTHOPEDIC CLINIC</text>
  </g>
</svg>
</body>
</html>
```